CREATE A BUSINESS CARD FOR A BOAT CLEANING SERVICE

WE ARE STARTING A NEW BOAT CLEANING BUSINESS. WE DIVE UNDERWATER TO CLEAN BOAT HULLS, JETTIES, UNDERWATER STRUCTURES ETC. WE ARE LOOKING FOR AN UPPERMARKET MODERN LOGO AND BUSINESS CARD AS ALOT OF OUR TARGET MARKET WILL BE HIGH END. YOU HAVE TO DESIGN A BUSINESS CARD AND LOGO SEPERATELY .
THE BUSINESS CARD DIMESNION MUST BE STANDARD SIZE.
The standard dimensions of a printed business card are 3.5 x 2 inches

Target Market(s)

UNDERWATER SERVICED

Industry/Entity Type

Business

Contact Information for Business Card

HALDEN UNDERWATER SERVICES

Font styles to use
Serif

Colors

Designer to choose colors to be used in the design.

Requirements
Must have
• HALDEN
Nice to have
• dark
Should not have
• more than 3 colors

```html
<!DOCTYPE html>
<html lang="en">
<head>
<meta charset="utf-8">
<title>Halden Underwater Service – Business Card</title>
<link href="https://fonts.googleapis.com/css2?family=Jost:wght@400;500&display=swap" rel="stylesheet">
<style>
  :root {
    --navy: #124e8a;
    --brand-blue: #1a4f8c;
    --wave-1: #c4d7ee;
    --wave-2: #8fb6e0;
    --wave-3: #5a9bd5;
    --wave-4: #2e86c8;
    --sky-top: #e6eef9;
    --grey-text: #555b63;
    --white: #ffffff;
    --card-edge: #8a8f96;
  }
  * { margin: 0; padding: 0; box-sizing: border-box; }
  html, body {
    width: 1200px; height: 1200px; overflow: hidden;
    background: var(--white);
    font-family: "Jost", sans-serif;
  }
  .business-card {
    position: absolute;
    left: 310px; top: 94px;
    width: 580px; height: 1010px;
    border: 1px solid var(--card-edge);
    overflow: hidden;
    background: linear-gradient(to bottom, var(--sky-top) 0%, var(--white) 45%);
  }
  .brand {
    position: absolute; top: 0; left: 0; width: 100%;
    text-align: center;
    color: var(--brand-blue);
  }
  .brand-name {
    position: absolute; top: 296px; width: 100%;
    font-size: 40px; font-weight: 500;
    letter-spacing: 0.32em; text-indent: 0.32em;
    color: var(--brand-blue);
  }
  .brand-tagline {
    position: absolute; top: 350px; width: 100%;
    font-size: 21px; font-weight: 400;
    letter-spacing: 0.14em; text-indent: 0.14em;
    color: var(--grey-text);
  }
  .waves {
    position: absolute; left: 0; top: 0;
    width: 580px; height: 1010px;
  }
  .contact {
    position: absolute; left: 0; top: 0; width: 100%;
    font-size: 26px; line-height: 32px;
  }
  .contact-person, .contact-phone {
    position: absolute; right: 324px; text-align: right; white-space: nowrap;
  }
  .contact-role, .contact-address {
    position: absolute; left: 290px; white-space: nowrap;
  }
  .contact-person { top: 654px; color: var(--brand-blue); }
  .contact-role { top: 654px; color: var(--brand-blue); }
  .contact-phone { top: 696px; color: var(--white); }
  .contact-address { top: 696px; color: var(--white); }
  .divider {
    position: absolute; left: 271px; width: 2px; background: var(--white);
  }
  .divider-top { top: 660px; height: 24px; }
  .divider-bottom { top: 702px; height: 24px; }
  .website {
    position: absolute; left: 0; top: 860px; width: 100%;
    text-align: center; font-size: 28px; color: var(--white);
  }
</style>
</head>
<body>
  <div class="business-card">
    <div class="brand">
      <div class="brand-name">HALDEN</div>
      <div class="brand-tagline">UNDERWATER SERVICE</div>
    </div>

    <svg class="waves" viewBox="0 0 580 1010" aria-hidden="true">
      <path fill="var(--wave-1)" d="M0,470 C180,470 320,590 580,570 L580,1010 L0,1010 Z"/>
      <path fill="var(--wave-2)" d="M0,546 C180,546 320,666 580,646 L580,1010 L0,1010 Z"/>
      <path fill="var(--wave-3)" d="M0,626 C180,626 320,746 580,726 L580,1010 L0,1010 Z"/>
      <path fill="var(--wave-4)" d="M0,716 C180,716 320,836 580,816 L580,1010 L0,1010 Z"/>
      <path fill="var(--navy)" d="M0,796 C180,796 320,916 580,896 L580,1010 L0,1010 Z"/>
    </svg>

    <div class="contact">
      <div class="contact-person">Marcus Dale</div>
      <div class="divider divider-top"></div>
      <div class="contact-role">Managing Director</div>
      <div class="contact-phone">+123 555 01942</div>
      <div class="divider divider-bottom"></div>
      <div class="contact-address">12, Reef Lane 4/2,<br>Harbour Heights,<br>40210 Brisbane,<br>Australia</div>
    </div>

    <div class="website">www.haldenunderwater.com</div>
  </div>
</body>
</html>
```